Coffee bag + cups: retail packaging

Our is seeking new packaging for a new coffee shop concept. As part of this we need to design new packaging for our coffee products. For this request, we are seeking design layouts for our retail bags and a cup for to-go coffee. We are working with 3 logo versions (pending final approval).

Please reference this website to see the types of coffee bag packaging options, there's a variety of bag options. We'd like the bag to be a Gusseted Bag, size 3.625 x 9.6 x 2.3125. We want a matte laminated material, not shiny.
https://www.brellumpack.com/

BAG
We'd like to see options of a black bag, blue, and kraft paper. Reference attached example.

Below is the text for our current bags, you can use that for now. I've attached example of bags that I like. We will look to you for design thoughts.

[Front]
Logo
100% Tanzanian
12oz
Dark Roast
Ground

[Back]
Amber Ridge Farms was established in 1989 by Marcus Ellery, son of baseball legend Thomas Ellery, and his family in rural Tanzania.
Today the coffee brand is sourced exclusively from the Ellery farm and other small scale family owned farms in Tanzania and East Africa.
This international coffee initiative is designed to bring a greater share of coffee revenues to farmers through direct trade and help develop rural communities in East Africa.

Visit us at Kelvorabeans.com

[Left panel]

Brewing instructions: Lorem ipsum dolor sit amet, consectetur adipiscing elit, sed do eiusmod tempor incididunt ut labore et dolore magna aliqua.

[Right panel]

Leave blank

Cup Sleeve
[Front of sleeve]
Logo

To-go cup
[Front]
Logo

Target Market(s)

Specialty coffee lovers.

Font styles to use
Serif
Sans Serif

Colors

Designer to choose colors to be used in the design.

Requirements
Must have
• Examples of coffee bag packaging.
• Must have; logo, text, clear and elegant labeling. Simple but strong.

```html
<!DOCTYPE html>
<html lang="en">
<head>
<meta charset="utf-8">
<title>Kelvora Coffee – Tanzania Packaging</title>
<link rel="stylesheet" href="https://fonts.googleapis.com/css2?family=Oswald:wght@500&family=Roboto+Condensed:wght@400;700&display=swap">
<style>
  :root {
    --backdrop: #eceeef;
    --kraft: #d6c2a0;
    --kraft-light: #e4d5bb;
    --label: #efe4d3;
    --lid: #cbb691;
    --lid-shade: #b9a27c;
    --ink: #2f1d14;
    --cocoa: #7a3f1e;
    --bean-light: #d8c29f;
    --bean-dark: #b0855c;
  }
  * { box-sizing: border-box; margin: 0; padding: 0; }
  html, body { width: 1200px; height: 923px; overflow: hidden; }
  body {
    background: var(--backdrop);
    position: relative;
    font-family: "Roboto Condensed", sans-serif;
    color: var(--ink);
  }

  /* Shared pieces */
  .origin { font-family: "Oswald", sans-serif; font-weight: 500; letter-spacing: 1px; line-height: 1; }
  .purity { letter-spacing: 3px; line-height: 1.1; }
  .brand { position: absolute; display: flex; align-items: center; gap: 8px; }
  .brand-mark { width: 22px; height: 22px; border-radius: 50%; background: var(--cocoa); flex: none; }
  .brand-name {
    font-family: "Oswald", sans-serif; font-weight: 500;
    line-height: 1; color: var(--ink); letter-spacing: 0.5px;
  }
  .bean-band {
    position: absolute; left: 0; right: 0; bottom: 0;
    background: linear-gradient(180deg, var(--bean-light) 0%, var(--bean-dark) 55%, var(--bean-light) 100%);
  }

  /* To-go cup */
  .cup-lid { position: absolute; left: 236px; top: 349px; }
  .cup {
    position: absolute; left: 250px; top: 404px;
    width: 220px; height: 367px;
    background: var(--kraft-light);
    clip-path: polygon(0 0, 100% 0, 92% 100%, 8% 100%);
  }
  .cup .brand { left: 44px; top: 100px; }
  .cup .brand-name { font-size: 34px; }
  .cup-band {
    position: absolute; left: 0; right: 0; top: 251px; height: 70px;
    background: var(--label);
    text-align: center; padding-top: 12px;
  }
  .cup-band .origin { font-size: 29px; }
  .cup-band .purity { font-size: 15px; margin-top: 2px; }
  .cup .bean-band { height: 46px; }

  /* Retail bag */
  .bag {
    position: absolute; left: 490px; top: 118px;
    width: 410px; height: 653px;
    background: var(--kraft);
  }
  .bag-seal {
    position: absolute; left: 0; right: 0; top: 78px; height: 2px;
    background: var(--lid-shade); opacity: 0.35;
  }
  .bag .brand { left: 24px; top: 345px; }
  .bag .brand-name { font-size: 36px; }
  .bag-label {
    position: absolute; left: 188px; top: 293px;
    width: 204px; height: 240px;
    background: var(--label);
    text-align: center; padding-top: 22px;
  }
  .bag-label .origin { font-size: 38px; }
  .bag-label .purity { font-size: 19px; margin-top: 4px; }
  .rule { width: 140px; height: 2px; background: var(--ink); margin: 6px auto 0; }
  .specs { display: flex; justify-content: center; align-items: flex-start; margin-top: 30px; text-align: left; }
  .specs .roast { font-size: 20px; line-height: 1.25; padding-right: 10px; border-right: 1.5px solid var(--ink); }
  .specs .roast b { font-weight: 700; }
  .specs .grind { padding-left: 10px; font-weight: 700; font-size: 20px; }
  .specs svg { display: block; margin-top: 4px; }
  .weight { position: absolute; left: 0; right: 0; bottom: 20px; font-size: 14px; }
  .bag .bean-band { height: 106px; }
</style>
</head>
<body>

  <svg class="cup-lid" width="248" height="58" viewBox="0 0 248 58" aria-hidden="true">
    <path d="M22 6 Q22 0 30 0 H218 Q226 0 226 6 V34 H22 Z" fill="#cbb691"/>
    <rect x="0" y="34" width="248" height="16" rx="6" fill="#bfa983"/>
    <rect x="12" y="50" width="224" height="8" fill="#b9a27c"/>
  </svg>

  <section class="cup" aria-label="To-go cup">
    <div class="brand">
      <span class="brand-mark"></span>
      <span class="brand-name">KELVORA<br>COFFEE</span>
    </div>
    <div class="cup-band">
      <p class="origin">TANZANIA</p>
      <p class="purity">100% PURE</p>
    </div>
    <div class="bean-band" role="img" aria-label="Hand-drawn coffee bean and leaf pattern"></div>
  </section>

  <section class="bag" aria-label="Retail coffee bag">
    <div class="bag-seal"></div>
    <div class="brand">
      <span class="brand-mark"></span>
      <span class="brand-name">KELVORA<br>COFFEE</span>
    </div>
    <div class="bag-label">
      <p class="origin">TANZANIA</p>
      <p class="purity">100% PURE</p>
      <div class="rule"></div>
      <div class="specs">
        <p class="roast">ROAST:<br><b>DARK</b></p>
        <div class="grind">
          <p>GROUND</p>
          <svg width="44" height="28" viewBox="0 0 44 28" aria-hidden="true">
            <path d="M2 2 L14 14" stroke="#2f1d14" stroke-width="2" fill="none"/>
            <path d="M12 12 L20 20 L26 14 Z" fill="none" stroke="#2f1d14" stroke-width="1.5"/>
            <circle cx="28" cy="6" r="1.5" fill="#2f1d14"/>
            <circle cx="33" cy="10" r="1.5" fill="#2f1d14"/>
            <circle cx="29" cy="13" r="1.5" fill="#2f1d14"/>
            <path d="M24 26 Q32 18 40 26 Z" fill="#2f1d14"/>
          </svg>
        </div>
      </div>
      <p class="weight">nett. wt.:12oz</p>
    </div>
    <div class="bean-band" role="img" aria-label="Hand-drawn coffee bean and leaf pattern"></div>
  </section>

</body>
</html>
```